Hello, I would like a small logo change and template for business cards.
It will be much like the "Les Perles de Mava", with following changes:.
1. The round shape stays the same
2. The color will be the brown version I already have
3. The wording will be "MAVA Organise"

Hello, 

So the "brown" is actually Pantone 126

Good luck

```html
<!DOCTYPE html>
<html lang="en">
<head>
<meta charset="utf-8">
<title>MAVA Organise – Business Card</title>
<link rel="stylesheet" href="https://fonts.googleapis.com/css2?family=Tenor+Sans&display=swap">
<style>
  :root {
    --pantone-126: #ad8505;
    --gold-light: #d6b97c;
    --gold-frame: #d9bd79;
    --gold-mid: #c8a253;
    --gold-text: #a88308;
    --cream-faint: #f4eddc;
    --ink: #555555;
    --caption: #333333;
    --page: #ffffff;
    --card-edge: #cfcfcf;
  }
  * { margin: 0; padding: 0; box-sizing: border-box; }
  html, body {
    width: 1200px; height: 1200px; overflow: hidden;
    background: var(--page);
    font-family: "Tenor Sans", "Optima", sans-serif;
  }
  .sheet { position: relative; width: 1200px; height: 1200px; }

  .card {
    position: absolute; left: 202px; width: 780px; height: 478px; overflow: hidden;
  }
  .card-back { top: 72px; background: var(--pantone-126); }
  .card-front { top: 630px; background: var(--page); border: 1.5px solid var(--card-edge); }

  .caption {
    position: absolute; left: 202px; width: 780px; text-align: center;
    font-size: 16px; color: var(--caption);
  }
  .caption-back { top: 583px; }
  .caption-front { top: 1131px; }

  /* back */
  .frame {
    position: absolute; left: 45px; top: 36px; width: 690px; height: 407px;
    border: 4px solid var(--gold-frame);
  }
  .frame-inner {
    position: absolute; inset: 6px;
    border: 2px solid var(--gold-frame);
    box-shadow: inset 0 0 10px rgba(90, 60, 0, 0.45);
  }

  .badge {
    position: absolute; border-radius: 50%;
    display: flex; align-items: center; justify-content: center; text-align: center;
  }
  .badge-back {
    left: 280px; top: 133px; width: 220px; height: 220px;
    background: var(--gold-light);
    box-shadow: 0 0 0 5px var(--pantone-126), 0 0 0 8px var(--gold-light);
  }
  .badge-front {
    left: 571px; top: 55px; width: 150px; height: 150px;
    background: var(--gold-mid);
    box-shadow: 0 0 0 3px var(--page), 0 0 0 5px var(--gold-mid);
  }
  .badge-name { line-height: 1.1; letter-spacing: 0.5px; }
  .badge-back .badge-name { font-size: 28px; color: var(--pantone-126); }
  .badge-front .badge-name { font-size: 19px; color: var(--page); }

  /* front */
  .watermark-area {
    position: absolute; left: 405px; top: 225px; width: 375px; height: 253px;
    background: linear-gradient(135deg, rgba(244, 237, 220, 0.25) 0%, var(--cream-faint) 55%, var(--cream-faint) 100%);
  }
  .holder-name {
    position: absolute; left: 75px; top: 118px;
    font-size: 33px; font-weight: 400; color: var(--gold-text);
  }
  .name-ornament {
    position: absolute; left: 45px; top: 172px; width: 60px; height: 16px;
    border-radius: 8px; background: var(--gold-light);
  }
  .contact {
    position: absolute; left: 75px; top: 268px;
    list-style: none; font-size: 20px; line-height: 30.5px; color: var(--ink);
  }
</style>
</head>
<body>
<main class="sheet">

  <section class="card card-back" aria-label="Card back">
    <div class="frame"><div class="frame-inner"></div></div>
    <div class="badge badge-back">
      <span class="badge-name">MAVA<br>Organise</span>
    </div>
  </section>
  <p class="caption caption-back">back</p>

  <section class="card card-front" aria-label="Card front">
    <div class="watermark-area" role="img" aria-label="Faint large script name watermark in pale cream"></div>
    <div class="badge badge-front">
      <span class="badge-name">MAVA<br>Organise</span>
    </div>
    <h1 class="holder-name">Full Name</h1>
    <div class="name-ornament" role="img" aria-label="Small row of gold pearl dots ornament"></div>
    <ul class="contact">
      <li>Address</li>
      <li>M : 0123 456 789</li>
      <li>T &nbsp;: +012 345 6789</li>
      <li>E &nbsp;: mava.organise@mava.com</li>
      <li>www.mava.com</li>
    </ul>
  </section>
  <p class="caption caption-front">front</p>

</main>
</body>
</html>
```